New emergency medical service needs a marketing flyer for prospective customers

We need a tri fold brochure on an 8.5 X 11 stock for a new emergency medical service in Pennsylvania. We provide basic first aid and now Covid-19 pre screening and temperature monitoring for special events, large gatherings and businesses. Examples of these would be but not limited to: Sporting events, carnivals, festivals, craft shows, warehouses, churches, manufacturing facilities, industrial buildings, large construction sites, multi occupancy officer buildings. The market for this is pretty much untouched and endless. we would like to use gray as the back ground color and obviously our logo. The final design should grab their attention and communicate the importance of having trained and certified professionals at their event or facility. We want to give them that piece of mind they are in good hands with us.

Target Market(s)

primary focus is going to be on businesses with large offices, large buildings or lots of foot traffic in and out of the building

Requirements
Must have
• gray background, pictures, company phone # , company web site, and contact email address. I will provide all that information to the winner to add at the end.
Nice to have
• pictures that covers the whole front cover with logo at top

```html
<!DOCTYPE html>
<html lang="en">
<head>
<meta charset="utf-8">
<title>Ridgeline Medical Services – Tri-fold Brochure Outside</title>
<link href="https://fonts.googleapis.com/css2?family=Raleway:wght@400;500;600;700;800&display=swap" rel="stylesheet">
<style>
  :root{
    --stage:#2b2b2c;
    --paper:#f1f1f2;
    --paper-mid:#f7f7f8;
    --navy:#1d1f7c;
    --teal:#17a991;
    --cyan:#52cfe6;
    --ink:#2a2a2c;
    --dark:#1f2023;
    --text:#3a3a3c;
    --silver-a:#b9b9bc;
    --silver-b:#f4f4f5;
    --pink:#e0457b;
  }
  *{box-sizing:border-box;margin:0;padding:0}
  html,body{width:794px;height:1200px;overflow:hidden}
  body{background:var(--stage);font-family:"Raleway",sans-serif;color:var(--text);position:relative}
  .brochure{position:absolute;left:20px;top:331px;width:754px;height:537px;background:var(--paper);overflow:hidden;box-shadow:0 8px 24px rgba(0,0,0,.45)}
  .panel-mid-bg{position:absolute;left:252px;top:0;width:250px;height:537px;background:var(--paper-mid)}
  .cover-photo{position:absolute;left:502px;top:114px;width:252px;height:300px;background:linear-gradient(160deg,#e9ece6 0%,#7c8a55 25%,#3d4a2c 48%,#262a4f 70%,#c9c8c2 100%)}
  .shapes{position:absolute;left:0;top:0;width:754px;height:537px}
  .photo-circle{position:absolute;border-radius:50%;background:linear-gradient(135deg,var(--silver-b),var(--silver-a) 60%,#e6e6e8);padding:6px}
  .photo-circle .fill{width:100%;height:100%;border-radius:50%}
  .circle-staff{left:301px;top:29px;width:154px;height:154px}
  .circle-staff .fill{background:linear-gradient(150deg,#e6eef2,#b8d7dc 45%,#4cc3c6 70%,#dfe7ea)}
  .circle-screening{left:30px;top:180px;width:194px;height:194px}
  .circle-screening .fill{background:linear-gradient(150deg,#c9b9a8,#e9e6e4 40%,#2d2d33 75%,#9fc3c6)}
  .tab{position:absolute;left:341px;top:0;width:75px;height:30px;background:linear-gradient(90deg,#c8c8cb,#e5e5e7)}
  .intro{position:absolute;left:23px;top:24px;width:215px}
  .intro h2{color:var(--teal);font-weight:500;font-size:14.6px;line-height:15.4px;width:192px}
  .intro p{font-size:7.4px;line-height:11px;margin-top:8px;color:#333;width:200px}
  .intro b{font-weight:700;color:#222}
  .services{position:absolute;left:23px;top:388px;width:215px;color:#fff}
  .services h3{font-size:11px;font-weight:600;letter-spacing:-.1px}
  .services h3 span{color:var(--teal)}
  .services .rule{width:42px;height:1px;background:var(--teal);margin:4px 0 8px}
  .services li{list-style:none;position:relative;padding-left:17px;font-size:7.9px;line-height:11.2px;margin-bottom:7px;color:#e8e8e8}
  .services li svg{position:absolute;left:0;top:2px;width:9px;height:9px}
  .footer-band{position:absolute;left:0;top:506px;width:754px;height:24px;background:linear-gradient(90deg,var(--silver-a),var(--silver-b) 20%,#c9c9cc 33%,var(--silver-b) 55%,#c5c5c8 70%,var(--silver-b) 88%,var(--silver-a))}
  .footer-band span{position:absolute;top:6px;font-size:8.6px;font-weight:600;letter-spacing:.9px;color:#222;width:250px;text-align:center}
  .footer-strip{position:absolute;left:330px;top:530px;width:424px;height:7px;background:var(--navy)}
  .feature{position:absolute;left:262px;top:187px;width:230px;text-align:center}
  .feature h2{font-size:14.6px;font-weight:600;line-height:16.5px;color:#555}
  .feature h2 span{display:block;color:var(--teal);font-weight:700}
  .feature p{font-size:7.6px;line-height:10.6px;margin-top:8px;color:#444}
  .quote-mark{position:absolute;left:358px;top:257px;font-size:44px;font-weight:800;color:#d3d3d5;line-height:1}
  .testimonial{position:absolute;left:288px;top:283px;width:180px;height:89px;border:1px dashed var(--pink);border-radius:12px;padding:12px 10px 0}
  .testimonial p{font-size:6.8px;line-height:10px;font-style:italic;text-align:center;color:#444}
  .client{position:absolute;left:330px;top:364px;width:96px;text-align:center;background:var(--paper-mid);font-size:10.4px;font-weight:700;color:var(--navy)}
  .contact{position:absolute;left:270px;top:428px;color:#fff}
  .contact h3{font-size:12px;font-weight:700}
  .contact .icons{display:flex;gap:6px;margin:9px 0 6px}
  .contact .icons svg{width:12px;height:12px}
  .contact p{font-size:7px;line-height:10px;color:#eee}
  .contact p b{font-weight:700}
  .follow{position:absolute;left:434px;top:477px;color:#fff;font-size:6.8px;font-weight:600}
  .follow .dots{display:flex;gap:3px;margin-top:4px}
  .follow .dots i{display:block;width:12px;height:12px;border-radius:50%;background:#fff}
  .brand{position:absolute;left:520px;top:30px;width:222px;text-align:center}
  .brand .mark{display:flex;align-items:center;justify-content:center;gap:7px}
  .brand .dot{width:30px;height:30px;border-radius:50%;background:var(--navy);flex:none}
  .brand .name{color:var(--navy);font-weight:800;font-size:19px;line-height:20px;text-align:left}
  .brand .tagline{color:var(--teal);font-size:8.3px;font-weight:500;margin-top:14px}
  .cover-copy{position:absolute;left:518px;top:412px;width:230px;color:#fff;z-index:2}
  .cover-copy .lead{color:var(--teal);font-size:9.4px;line-height:11px;font-weight:500}
  .cover-copy h1{font-size:18.5px;line-height:18.6px;font-weight:800;margin-top:5px;letter-spacing:-.2px}
</style>
</head>
<body>
<main class="brochure">
  <div class="panel-mid-bg"></div>
  <div class="cover-photo" role="img" aria-label="Photo: paramedics attending to a patient on a stretcher beside an ambulance"></div>

  <svg class="shapes" viewBox="0 0 754 537" aria-hidden="true">
    <polygon points="0,365 115,323 205,348 430,458 586,364 754,318 754,537 0,537" fill="#1f2023"/>
    <polygon points="330,537 586,362 754,425 754,537" fill="#1d1f7c"/>
    <polygon points="423,458 505,402 509,407 427,463" fill="#52cfe6"/>
    <polygon points="0,362 48,344 50,350 0,369" fill="#52cfe6"/>
  </svg>

  <div class="tab"></div>
  <div class="photo-circle circle-staff"><div class="fill" role="img" aria-label="Photo: smiling nurse in teal scrubs holding a clipboard"></div></div>
  <div class="photo-circle circle-screening"><div class="fill" role="img" aria-label="Photo: staff in face masks having temperature checked with an infrared thermometer"></div></div>

  <section class="intro">
    <h2>We provide basic first aid and now Covid-19 pre screening and temperature monitoring for special events.</h2>
    <p>Large gatherings and businesses. Examples of these would be but not limited to: <b>Sporting events, carnivals, festivals, craft shows, warehouses, churches, manufacturing facilities, industrial buildings, large construction sites, multi occupancy officer buildings.</b></p>
  </section>

  <section class="services">
    <h3><span>LOREM IPSUM</span> SIMPLY DUMMY TEXT</h3>
    <div class="rule"></div>
    <ul>
      <li><svg viewBox="0 0 10 10"><circle cx="5" cy="5" r="4.3" fill="none" stroke="#17a991" stroke-width="1"/><path d="M3 5.2l1.4 1.4L7.2 3.8" fill="none" stroke="#17a991" stroke-width="1"/></svg>Lorem Ipsum is simply dummy text of the printing and typesetting industry.</li>
      <li><svg viewBox="0 0 10 10"><circle cx="5" cy="5" r="4.3" fill="none" stroke="#17a991" stroke-width="1"/><path d="M3 5.2l1.4 1.4L7.2 3.8" fill="none" stroke="#17a991" stroke-width="1"/></svg>Lorem Ipsum has been the industry's standard dummy text ever since the 1500s,</li>
      <li><svg viewBox="0 0 10 10"><circle cx="5" cy="5" r="4.3" fill="none" stroke="#17a991" stroke-width="1"/><path d="M3 5.2l1.4 1.4L7.2 3.8" fill="none" stroke="#17a991" stroke-width="1"/></svg>When an unknown printer took a galley of type and scrambled it to make a type specimen book.</li>
    </ul>
  </section>

  <section class="feature">
    <h2>LOREM IPSUM <span>SIMPLY DUMMY TEXT</span></h2>
    <p>Lorem Ipsum is simply dummy text of the printing and typesetting industry. Lorem Ipsum has been the industry's standard dummy text ever since the 1500s,</p>
  </section>
  <div class="quote-mark">&ldquo;</div>
  <blockquote class="testimonial">
    <p>Lorem Ipsum is simply dummy text of the printing and typesetting industry. Lorem Ipsum has been the industry's standard dummy text ever since the 1500s, when an unknown printer took a galley of type and scrambled it to make a type specimen book.</p>
  </blockquote>
  <div class="client">Client Name</div>

  <section class="contact">
    <h3>Get in Touch</h3>
    <div class="icons">
      <svg viewBox="0 0 12 12"><circle cx="6" cy="6" r="6" fill="#27a9e1"/><path d="M6 2.6a2.2 2.2 0 0 0-2.2 2.2C3.8 6.5 6 9.4 6 9.4s2.2-2.9 2.2-4.6A2.2 2.2 0 0 0 6 2.6z" fill="#1f2023"/><circle cx="6" cy="4.8" r=".8" fill="#27a9e1"/></svg>
      <svg viewBox="0 0 12 12"><circle cx="6" cy="6" r="6" fill="#27a9e1"/><path d="M4.1 3c.4 0 .9 1.2.9 1.5s-.5.5-.5.8c0 .5 1.7 2.2 2.2 2.2.3 0 .5-.5.8-.5s1.5.5 1.5.9c0 .6-.8 1.1-1.4 1.1C5.9 9 3 6.1 3 4.4 3 3.8 3.5 3 4.1 3z" fill="#1f2023"/></svg>
      <svg viewBox="0 0 12 12"><circle cx="6" cy="6" r="6" fill="#27a9e1"/><rect x="3" y="4" width="6" height="4.2" fill="none" stroke="#1f2023" stroke-width=".9"/><path d="M3 4l3 2.4L9 4" fill="none" stroke="#1f2023" stroke-width=".9"/></svg>
    </div>
    <p>Your Company Address Goes Here<br><b>0123 456 789</b><br>info@yourmailid.com</p>
  </section>

  <div class="follow">Follow Us on
    <div class="dots"><i></i><i></i><i></i></div>
  </div>

  <header class="brand">
    <div class="mark"><span class="dot"></span><span class="name">Ridgeline<br>Medical Services</span></div>
    <p class="tagline">Emergency medical service in Pennsylvania</p>
  </header>

  <section class="cover-copy">
    <p class="lead">Provide certified<br>medical professionals for</p>
    <h1>MEDICAL<br>STANDBYS AT<br>EVENTS &amp; BUSINESSES.</h1>
  </section>

  <div class="footer-band">
    <span style="left:0">Mail us : Info@yourmailid.com</span>
    <span style="left:252px">Visit Us : www.yourwebsite.com</span>
    <span style="left:504px;letter-spacing:.3px">CALL US : 0123 456 789</span>
  </div>
  <div class="footer-strip"></div>
</main>
</body>
</html>
```